Colin Marsh Optometry "we are moving" - to be used as a business card size magnet

Our optometry business "Colin Marsh Optometry" is moving location at the end of 2017. We plan to have business card size magnets printed to hand to our current customers to remind them that we are moving at the end of this year. We would like a clean, simple design that uses our logo and colour branding (see uploaded business card) with our new address "42 Carrow Lane Wrenfield" our phone number "6827 1054" and "same great people, same great service" and "just next to the Silver Lark Dentist".

```html
<!DOCTYPE html>
<html lang="en">
<head>
<meta charset="utf-8">
<title>Colin Marsh Optometry – Moving Magnet</title>
<link rel="stylesheet" href="https://fonts.googleapis.com/css2?family=Source+Sans+3:ital,wght@0,400;0,600;1,400;1,700&display=swap">
<style>
  :root {
    --plum: #54435b;
    --plum-mid: #7b6a82;
    --plum-light: #a597ab;
    --paper: #ffffff;
    --backdrop: #e9e7ea;
    --ink: #4a3a52;
  }
  * { margin: 0; padding: 0; box-sizing: border-box; }
  html, body {
    width: 1200px; height: 1000px; overflow: hidden;
    background: var(--backdrop);
    font-family: "Source Sans 3", sans-serif;
  }
  .magnet {
    position: absolute; left: 150px; top: 227px;
    width: 900px; height: 546px;
    background: var(--paper);
    overflow: hidden;
    box-shadow: 0 10px 30px rgba(60, 40, 70, 0.18);
  }
  .magnet__swoosh { position: absolute; inset: 0; width: 900px; height: 546px; }
  .brand {
    position: absolute; left: 172px; top: 72px;
    color: var(--ink); line-height: 1;
  }
  .brand__name { font-size: 32px; font-weight: 400; display: block; }
  .brand__trade { font-size: 58px; font-weight: 600; display: block; margin-top: 2px; letter-spacing: -0.5px; }
  .contact { position: absolute; left: 46px; top: 247px; color: var(--ink); font-weight: 600; }
  .contact__row { display: flex; align-items: center; gap: 21px; height: 48px; font-size: 29px; letter-spacing: 0.5px; }
  .contact__row + .contact__row { margin-top: 17px; }
  .contact__icon { width: 48px; height: 48px; flex: none; }
  .address {
    position: absolute; left: 50px; top: 380px;
    color: var(--ink); font-weight: 600; font-style: normal;
    font-size: 29px; line-height: 38px; letter-spacing: 0.3px;
  }
  .message {
    position: absolute; left: 556px; top: 246px; width: 300px;
    text-align: center; color: var(--paper); line-height: 1;
  }
  .message__same { font-style: italic; font-weight: 400; font-size: 35px; display: block; margin-bottom: 2px; }
  .message__strong { font-style: italic; font-weight: 700; font-size: 25px; display: block; margin-bottom: 8px; }
  .message__soft { font-style: italic; font-weight: 400; font-size: 25px; display: block; margin-bottom: 9px; }
</style>
</head>
<body>
  <article class="magnet">
    <svg class="magnet__swoosh" viewBox="0 0 900 546" aria-hidden="true">
      <path d="M231,546 C420,430 640,150 850,0 L900,0 L900,546 Z" fill="var(--plum-light)"/>
      <path d="M285,546 C460,430 680,160 900,10 L900,546 Z" fill="var(--plum-mid)"/>
      <path d="M350,546 C510,440 720,190 900,40 L900,546 Z" fill="var(--plum)"/>
    </svg>

    <h1 class="brand">
      <span class="brand__name">Colin Marsh</span>
      <span class="brand__trade">Optometry</span>
    </h1>

    <div class="contact">
      <div class="contact__row">
        <svg class="contact__icon" viewBox="0 0 48 48" aria-hidden="true">
          <circle cx="24" cy="24" r="21" fill="none" stroke="var(--ink)" stroke-width="3"/>
          <path d="M14 21 Q24 12 34 21 L31 24 L28 21 L20 21 L17 24 Z" fill="var(--ink)"/>
          <rect x="17" y="23" width="14" height="11" rx="2" fill="var(--ink)"/>
        </svg>
        <span>6827 1054</span>
      </div>
      <div class="contact__row">
        <svg class="contact__icon" viewBox="0 0 48 48" aria-hidden="true">
          <circle cx="24" cy="24" r="21" fill="none" stroke="var(--ink)" stroke-width="3"/>
          <path d="M31 15 L17 20 L22 23 L16 30 L19 33 L26 27 L29 32 Z" fill="var(--ink)"/>
        </svg>
        <span>colinmarsh.com.au</span>
      </div>
    </div>

    <address class="address">42 Carrow Lane<br>Wrenfield</address>

    <p class="message">
      <span class="message__same">same</span>
      <span class="message__strong">great people</span>
      <span class="message__same">same</span>
      <span class="message__strong">great service</span>
      <span class="message__soft">and</span>
      <span class="message__soft">just next to the</span>
      <span class="message__strong">Silver Lark Dentist</span>
    </p>
  </article>
</body>
</html>
```